Airport Advertising Brochure

I need a flyer put together asap! Previous example included. Would like something clean and updated. New logo and updated company name. I would like this designed in Pages or Illustrator so I can update content when needed. Website: pagelantern.com

Target Market(s)

Authors. This page has some good content about what we do: https://www.pagelantern.com/terminaladvertising/

Industry/Entity Type

Airport

Font styles to use
Serif
Sans Serif

Requirements
Must have
• Clean, modern design.

```html
<!DOCTYPE html>
<html lang="en">
<head>
<meta charset="utf-8">
<title>Terminal Advertising – Page Lantern</title>
<link rel="stylesheet" href="https://fonts.googleapis.com/css2?family=Inter:wght@400;700;800&display=swap">
<style>
  :root {
    --ink: #000000;
    --signal-yellow: #ffe600;
    --stripe-yellow: #fff3a3;
    --frame-yellow: #fdeb8c;
    --panel-top: #e4e4e4;
    --panel-mid: #ffffff;
    --body-text: #2e2e2e;
  }
  html, body {
    margin: 0;
    padding: 0;
    width: 1200px;
    height: 900px;
    overflow: hidden;
    background: var(--frame-yellow);
  }
  .flyer {
    display: block;
    width: 1200px;
    height: 900px;
    font-family: "Inter", Arial, sans-serif;
  }
  .headline {
    fill: var(--signal-yellow);
    font-weight: 800;
    font-size: 62px;
  }
  .site-url {
    fill: var(--signal-yellow);
    font-weight: 400;
    font-size: 23px;
  }
  .offer-title {
    fill: var(--body-text);
    font-weight: 700;
    font-size: 32px;
  }
  .offer-line {
    fill: var(--body-text);
    font-weight: 400;
    font-size: 21.5px;
  }
</style>
</head>
<body>
<svg class="flyer" viewBox="0 0 1200 900" xmlns="http://www.w3.org/2000/svg" role="img" aria-label="Page Lantern terminal advertising packages">
  <defs>
    <linearGradient id="panelShade" x1="0" y1="0" x2="0" y2="1">
      <stop offset="0" stop-color="var(--panel-top)"/>
      <stop offset="0.35" stop-color="var(--panel-mid)"/>
      <stop offset="0.8" stop-color="var(--panel-mid)"/>
      <stop offset="1" stop-color="#e8e8e8"/>
    </linearGradient>
  </defs>

  <!-- background frame -->
  <rect class="frame" width="1200" height="900" fill="var(--frame-yellow)"/>

  <!-- info panel -->
  <polygon class="info-panel" points="600,24 1176,24 1176,876 428,876" fill="url(#panelShade)"/>

  <!-- diagonal accent stripes -->
  <polygon class="accent-stripe-soft" points="596,0 612,0 420,900 392,900" fill="var(--stripe-yellow)"/>
  <polygon class="accent-stripe" points="600,0 616,0 398,900 352,900" fill="var(--signal-yellow)"/>

  <!-- dark title block -->
  <polygon class="title-block" points="0,0 606,0 352,900 0,900" fill="var(--ink)"/>

  <!-- headline -->
  <g class="headline">
    <text x="70" y="172" textLength="462" lengthAdjust="spacingAndGlyphs">Window Display,</text>
    <text x="70" y="238.4" textLength="315" lengthAdjust="spacingAndGlyphs">Front Table</text>
    <text x="70" y="305.6" textLength="214" lengthAdjust="spacingAndGlyphs">Display,</text>
    <text x="70" y="370.4" textLength="102" lengthAdjust="spacingAndGlyphs">and</text>
    <text x="70" y="437.6" textLength="250" lengthAdjust="spacingAndGlyphs">Business</text>
    <text x="70" y="504" textLength="187" lengthAdjust="spacingAndGlyphs">Center</text>
    <text x="70" y="570.4" textLength="219" lengthAdjust="spacingAndGlyphs">Pockets</text>
  </g>

  <text class="site-url" x="70" y="838" textLength="256" lengthAdjust="spacingAndGlyphs">www.pagelantern.com</text>

  <!-- offer: front table -->
  <g class="offer offer-front-table">
    <text class="offer-title" x="610" y="138.4">Front of Store Table Placement</text>
    <text class="offer-line" x="604" y="165.6">· 26 bookstores (including: Harlow-Jameson Ashford</text>
    <text class="offer-line" x="597.6" y="193.6">International Airport, Penbrook International Airport,</text>
    <text class="offer-line" x="592" y="221.6">Jasperville International Airport, Sprague Falls</text>
    <text class="offer-line" x="586.4" y="249.6">International Airport, Palm Harbor Coastal International</text>
    <text class="offer-line" x="581.6" y="277.6">Airport, and more)</text>
    <text class="offer-line" x="576" y="305.6">· 1 month</text>
  </g>

  <!-- offer: window display -->
  <g class="offer offer-window">
    <text class="offer-title" x="564" y="374.4">· Window Display</text>
    <text class="offer-line" x="557.6" y="401.6">· 26 bookstores (including: O’Malley International Airport,</text>
    <text class="offer-line" x="552" y="429.6">Los Alamar International Airport, Dalton Lovecrest</text>
    <text class="offer-line" x="545.6" y="457.6">International</text>
    <text class="offer-line" x="540.8" y="485.6">Airport, Seaview Tacora International Airport, Lorman</text>
    <text class="offer-line" x="535.2" y="513.6">International Airport, Delvin International Airport, and more)</text>
    <text class="offer-line" x="529.6" y="541.6">· 3 months</text>
    <text class="offer-line" x="524" y="569.6">· Plus Spine out placement of book in business section of</text>
    <text class="offer-line" x="518.4" y="597.6">store</text>
  </g>

  <!-- offer: business center pocket -->
  <g class="offer offer-pocket">
    <text class="offer-title" x="506.4" y="666.4">· Business Center Pocket</text>
    <text class="offer-line" x="500" y="693.6">· 28 bookstores (including: Los Alamar International Airport,</text>
    <text class="offer-line" x="494.4" y="721.6">Penbrook International Airport, Carlotta International</text>
    <text class="offer-line" x="489.6" y="749.6">Airport, San Delmar International Airport, Harlow-Jameson</text>
    <text class="offer-line" x="483.2" y="777.6">International Airport, and more)</text>
    <text class="offer-line" x="478.4" y="805.6">· 1 month</text>
  </g>
</svg>
</body>
</html>
```